Business Card Design Project

A new design for our business cards for a small casting/talent agency, we would like to incorporate the logo and brand colors within the design, below are the information that should be on the card

(Name)
(Title)

Corvel Arta FZ-LLC
Brindle Quay Park
Building 27, Suite 418
Dubai, UAE
PO Box 871465
+97140000000
info@CorvelArta-example.com

Target Market(s)

production companies, film makers, media, entertainment industry

Industry/Entity Type

Business

Requirements
Must have
• logo, logo colors
Nice to have
• cutting edge design, sleek and modern
Should not have
• playful, funky, congested

```html
<!DOCTYPE html>
<html lang="en">
<head>
<meta charset="utf-8">
<title>Corvel Arta – Business Card</title>
<link rel="stylesheet" href="https://fonts.googleapis.com/css2?family=Arimo:wght@400;700&display=swap">
<style>
  :root {
    --backdrop: #2b2b2d;
    --card-grey: #7b7b7d;
    --navy: #1d2d5c;
    --navy-deep: #172550;
    --mist: #b7c0cc;
    --white: #ffffff;
    --rule: rgba(255, 255, 255, 0.55);
  }
  * { box-sizing: border-box; margin: 0; padding: 0; }
  html, body {
    width: 1200px;
    height: 900px;
    overflow: hidden;
    background: var(--backdrop);
    font-family: "Arimo", Arial, sans-serif;
  }
  .canvas {
    position: relative;
    width: 1200px;
    height: 900px;
  }
  .card {
    position: absolute;
    width: 620px;
    height: 354px;
    border-radius: 3px;
    overflow: hidden;
    box-shadow: 0 14px 34px rgba(0, 0, 0, 0.45);
  }

  /* Front side */
  .card-front {
    left: 90px;
    top: 80px;
    background: var(--card-grey);
  }
  .brand-badge {
    position: absolute;
    left: 50%;
    top: 50%;
    width: 210px;
    height: 210px;
    margin: -105px 0 0 -105px;
    border-radius: 50%;
    background: var(--navy);
    display: flex;
    align-items: center;
    justify-content: center;
  }
  .brand-name {
    color: var(--mist);
    font-weight: 400;
    font-size: 30px;
    letter-spacing: 0.5px;
  }

  /* Back side */
  .card-back {
    left: 490px;
    top: 466px;
    background: var(--navy);
    color: var(--white);
  }
  .person {
    position: absolute;
    left: 44px;
    top: 52px;
  }
  .person-name {
    font-weight: 700;
    font-size: 20px;
    letter-spacing: 0.6px;
    color: var(--mist);
  }
  .person-title {
    font-size: 12px;
    color: var(--mist);
    margin-top: 3px;
  }
  .info-block {
    position: absolute;
    left: 60px;
    border-left: 1px solid var(--rule);
    padding-left: 14px;
    font-size: 13px;
    line-height: 1.3;
    color: var(--white);
  }
  .address { top: 118px; }
  .address .company { font-weight: 700; color: var(--mist); }
  .address .gap { margin-top: 8px; }
  .contact { top: 262px; }
  .brand-mark-space {
    position: absolute;
    right: 48px;
    top: 62px;
    width: 230px;
    height: 230px;
    border-radius: 50%;
    background: var(--navy-deep);
    border: 2px solid rgba(183, 192, 204, 0.35);
  }
</style>
</head>
<body>
<main class="canvas">
  <section class="card card-front" aria-label="Card front">
    <div class="brand-badge">
      <span class="brand-name">Corvel Arta</span>
    </div>
  </section>

  <section class="card card-back" aria-label="Card back">
    <div class="person">
      <p class="person-name">MARA ELLISON</p>
      <p class="person-title">General Manager</p>
    </div>
    <address class="info-block address">
      <p class="company">Corvel Arta FZ-LLC</p>
      <p>Brindle Quay Park</p>
      <p class="gap">Building 27, Suite 418</p>
      <p>Dubai, UAE</p>
      <p>PO Box 871465</p>
    </address>
    <address class="info-block contact">
      <p>+97140000000</p>
      <p>info@CorvelArta-example.com</p>
      <p>www.CorvelArta-example.com</p>
    </address>
    <div class="brand-mark-space" role="img" aria-label="Space reserved for the brand mark"></div>
  </section>
</main>
</body>
</html>
```